Business Card

Need business cards and small flyers for a musical band

Target Market(s)

Promoters, clients seeking to hire a Latin band

Industry/Entity Type

Business

Requirements
Must have
• The name of the band is Orchestra Brisa so want to have the background with a fire design, with black card and the name of the band in RED, maybe a combination of Red with some yellow. See attached idea.
Nice to have
• See attached files for some ideas.

```html
<!DOCTYPE html>
<html lang="en">
<head>
<meta charset="utf-8">
<title>Orchestra Brisa – Business Card</title>
<link rel="stylesheet" href="https://fonts.googleapis.com/css2?family=Baloo+2:wght@600;800&family=Cinzel+Decorative:wght@700&display=swap">
<style>
  :root {
    --card-black: #050303;
    --accent-red: #c4262c;
    --flame-red: #d7261a;
    --flame-orange: #f26a12;
    --flame-yellow: #ffd24a;
    --contact-yellow: #f7c94a;
    --contact-shadow: #2a0a02;
  }
  * { margin: 0; padding: 0; box-sizing: border-box; }
  html, body {
    width: 1200px;
    height: 669px;
    overflow: hidden;
    background: var(--card-black);
  }
  .card {
    position: relative;
    width: 1200px;
    height: 669px;
    background: var(--card-black);
    overflow: hidden;
  }
  .flame-field {
    position: absolute;
    left: 0;
    top: 320px;
    width: 1200px;
    height: 349px;
    background:
      radial-gradient(ellipse 420px 220px at 200px 360px, rgba(255,170,40,.85), rgba(230,70,20,.55) 45%, transparent 75%),
      radial-gradient(ellipse 520px 200px at 900px 380px, rgba(255,190,60,.8), rgba(220,60,20,.5) 50%, transparent 80%),
      radial-gradient(ellipse 380px 160px at 560px 330px, rgba(200,40,20,.6), transparent 75%),
      linear-gradient(to bottom, transparent 0%, rgba(120,20,10,.45) 35%, rgba(210,70,20,.75) 75%, rgba(240,140,40,.85) 100%);
  }
  .clef-flame {
    position: absolute;
    left: 90px;
    top: 45px;
    width: 217px;
    height: 400px;
    border-radius: 45% 45% 40% 40%;
    background: radial-gradient(ellipse at 50% 65%, rgba(255,210,90,.95), rgba(240,110,25,.8) 40%, rgba(170,30,15,.45) 70%, transparent 85%);
  }
  .title-rule {
    position: absolute;
    left: 404px;
    top: 83px;
    width: 495px;
    height: 2px;
    background: var(--accent-red);
  }
  .band-label {
    position: absolute;
    right: 42px;
    top: 54px;
    font-family: "Baloo 2", sans-serif;
    font-weight: 600;
    font-size: 46px;
    line-height: 1;
    color: var(--accent-red);
  }
  .band-name {
    position: absolute;
    left: 404px;
    top: 190px;
    width: 760px;
    display: flex;
    justify-content: space-between;
    font-family: "Cinzel Decorative", serif;
    font-weight: 700;
    font-size: 104px;
    line-height: 1;
  }
  .band-name span {
    background: linear-gradient(to bottom, var(--flame-yellow) 0%, var(--flame-orange) 50%, var(--flame-red) 100%);
    -webkit-background-clip: text;
    background-clip: text;
    color: transparent;
    filter: drop-shadow(0 0 14px rgba(215,38,26,.7));
  }
  .contact {
    position: absolute;
    right: 44px;
    top: 488px;
    text-align: right;
    font-family: "Baloo 2", sans-serif;
    font-weight: 800;
    font-size: 41px;
    line-height: 74px;
    color: var(--contact-yellow);
    text-shadow: 2px 2px 0 var(--contact-shadow), 0 0 6px var(--contact-shadow);
  }
</style>
</head>
<body>
  <main class="card">
    <div class="flame-field" role="img" aria-label="Wall of rising orange and yellow flames across the lower card"></div>
    <div class="clef-flame" role="img" aria-label="Treble clef formed from flames"></div>

    <div class="title-rule"></div>
    <p class="band-label">Orchestra</p>
    <h1 class="band-name" aria-label="Brisa">
      <span>B</span><span>R</span><span>I</span><span>S</span><span>A</span>
    </h1>

    <div class="contact">
      <p class="contact-email">e-mail:brisaband47@mailbox.com</p>
      <p class="contact-phone">Cell phone: 813-555-0147</p>
    </div>
  </main>
</body>
</html>
```